Informational Landing Page Redesign

Purebrook Filter Guide, reviews and provides information about water ionizers for users. The web site is supposed to be an "expert or researched based" We are looking to redesign the following landing page:

http://www.purebrookfilterguide-example.com/learn/what-is-pure-flow

The design should be geared towards converting visitors into leads. We are looking for a redesign of the content section. The header and footer should be the same as the current site. The text and colors should be consistent with the current site but please feel free to make bold choices that work and add stock photos.

Target Market(s)

Ages 45+ with disposable income.

Industry/Entity Type

Learn

Requirements
Must have
• The page must have the all current content. It also should have a web site form placed above the fold.

Please note you can change the designs of the "advertisements".
Nice to have
• Placement of social media elements so users can spread the page to friends, example facebook and google+ like buttons. A banner area that is capable of holding a rotating banner or video or banner.
Should not have
• Distractions from the goal, converting users to leads.
Distractions from the content, since the user is there to read.
Missing information and text, all information on the current page should appear on the redesign.

Deviations from the current header and footer.

```html
<!DOCTYPE html>
<html lang="en">
<head>
<meta charset="utf-8">
<title>What is Alkaline Water? – Purebrook Filter Guide</title>
<link rel="stylesheet" href="https://fonts.googleapis.com/css2?family=Open+Sans:ital,wght@0,400;0,600;0,700;0,800;1,400&family=Libre+Baskerville:wght@700&display=swap">
<style>
:root{
  --page:#f0efee;
  --white:#ffffff;
  --blue:#1b7fc3;
  --blue-band:#2189cf;
  --blue-dark:#0f5f99;
  --orange:#f58a07;
  --text:#444444;
  --muted:#666666;
  --rule:#d6d6d6;
  --green:#6fae1d;
  --yellow:#ffe000;
}
*{box-sizing:border-box;margin:0;padding:0}
html,body{width:918px;height:1200px;overflow:hidden}
body{background:var(--page);font-family:"Open Sans",Arial,sans-serif;color:var(--text);position:relative}
a{color:var(--blue);text-decoration:none}

/* header */
.brand{position:absolute;display:flex;align-items:flex-start;gap:8px}
.brand-dot{width:34px;height:34px;border-radius:50%;background:var(--blue-band);margin-top:14px}
.brand-name{font-weight:600;color:#6b6b6b;font-size:19px;line-height:21px;letter-spacing:.3px;white-space:nowrap}
.brand-tag{font-size:10px;color:#6b6b6b;margin-top:4px;white-space:nowrap}
.site-brand{left:140px;top:16px}
.main-nav{position:absolute;left:364px;top:16px;width:417px;height:27px;background:#f4f4f4;border-top:1px solid var(--rule);border-bottom:1px solid var(--rule);display:flex;justify-content:space-around;align-items:center}
.main-nav a{font-weight:700;font-size:13px;color:var(--blue);letter-spacing:.2px}
.btn-guide{position:absolute;left:696px;top:51px;width:85px;height:25px;background:var(--orange);color:#fff;font-weight:700;font-size:10px;border-radius:3px;display:flex;align-items:center;justify-content:center}

/* hero */
.hero{position:absolute;left:137px;top:117px;width:443px;height:233px;background:var(--white);border:2px solid #d9d9d9;overflow:hidden}
.hero-title{position:absolute;left:22px;top:30px;font-size:14.5px;line-height:18px;color:#333;font-weight:400;letter-spacing:.2px}
.hero-sub{position:absolute;left:22px;top:79px;font-size:10.5px;line-height:14px;color:#222}
.hero-art{position:absolute;left:0;top:100px;width:100%;height:131px;background:linear-gradient(180deg,#ffffff 0%,#cfe6f7 25%,#5fb0e6 60%,#1d6fba 100%)}
.hero-bottles{position:absolute;right:14px;top:46px;width:120px;height:185px;background:linear-gradient(180deg,#e6eef5,#9fb8cc);border-radius:6px;opacity:.7}

/* sidebar */
.lead-form{position:absolute;left:601px;top:116px;width:181px;height:235px;background:var(--white);border:1px solid #dcdcdc}
.band{background:var(--blue-band);color:#fff;font-weight:800}
.lead-form .band{height:36px;font-size:19px;text-align:right;padding:3px 10px 0 0;font-family:Arial,sans-serif}
.lead-form h3{color:var(--blue-dark);font-size:16px;line-height:18.5px;text-align:center;font-weight:700;margin:9px 4px 4px;letter-spacing:.5px}
.field{display:flex;align-items:center;justify-content:space-between;padding:0 8px 0 7px;height:27px}
.field label{font-size:10px;font-weight:700;color:#333}
.field span{width:118px;height:16px;border:1px solid #cfcfcf;background:#fff}
.btn-download{position:absolute;right:7px;bottom:10px;width:104px;height:28px;background:var(--orange);color:#fff;font-weight:700;font-size:17px;border-radius:3px;display:flex;align-items:center;justify-content:center}

.learn-box{position:absolute;left:600px;top:370px;width:182px;height:190px;background:var(--white);border:1px solid #dcdcdc}
.learn-box .band{height:49px;font-size:21px;padding:11px 0 0 10px;font-family:Arial,sans-serif;font-weight:700}
.learn-box ul{list-style:none;padding:0 32px 0 10px}
.learn-box li{border-bottom:1px solid #e2e2e2;padding:3px 0 4px;font-size:11px;font-weight:600;line-height:16px;white-space:nowrap}
.learn-box li:last-child{border-bottom:0}

.ad-label{position:absolute;left:604px;top:577px;font-size:8px;color:#555}
.ad{position:absolute;background:var(--white);border:1px solid #d4d4d4;overflow:hidden}
.ad-lifestyle{left:601px;top:593px;width:180px;height:213px}
.ad-lifestyle .ad-art{position:absolute;inset:0;background:linear-gradient(160deg,#ffffff 30%,#e4f3c8 65%,#bfe08a 100%)}
.ad-lifestyle .ad-head{position:absolute;left:14px;top:2px;font-family:Arial,sans-serif;font-weight:800;font-size:22px;line-height:22px;color:#4b3f8a}
.ad-word{position:absolute;font-weight:700;color:#7aa520;white-space:nowrap;line-height:20px}
.w-nutrition{left:8px;top:98px;font-size:18px}
.w-mind{left:34px;top:152px;font-size:12px}
.w-fitness{right:8px;top:128px;font-size:15px}
.btn-join{position:absolute;left:26px;bottom:5px;width:128px;height:30px;background:var(--green);border:2px solid #e6f0d6;color:#fff;font-weight:700;font-size:15px;border-radius:3px;display:flex;align-items:center;justify-content:center}

.ad-deals{left:602px;top:827px;width:178px;height:259px;background:linear-gradient(180deg,#0e5a94,#1d8fd6 45%,#0c5f9f);border:1px solid #c9c9c9;color:#fff;text-align:center}
.ad-deals .deal-top{height:49px;background:#0e4f82;font-size:14px;line-height:18px;padding-top:7px;font-weight:400}
.ad-deals .deal-top b{font-weight:600}
.ad-deals .guarantee{font-family:Arial,sans-serif;font-weight:800;font-size:21px;line-height:28px;margin-top:3px;letter-spacing:.3px}
.ad-deals .product{width:140px;height:106px;margin:2px auto 0;background:linear-gradient(180deg,#d7e4ee,#8fa8bb);border-radius:6px}
.ad-deals .talk{font-size:13px;line-height:16px;margin-top:6px}
.ad-deals .phone{font-size:16.5px;line-height:20px;font-weight:700;color:var(--yellow)}
.ad-deals .web{font-size:10px;line-height:14px;font-weight:700;margin-top:3px}

/* social */
.share-col{position:absolute;left:86px;top:412px;width:38px;display:flex;flex-direction:column;align-items:center;font-size:8.5px;color:#333}
.count{width:36px;height:24px;background:#fff;border:1px solid #d4d4d4;border-radius:3px;display:flex;align-items:center;justify-content:center;font-size:11px}
.share-btn{display:flex;align-items:center;gap:2px;margin:3px 0 9px;font-weight:600}
.share-btn i{width:7px;height:7px;background:var(--blue);display:inline-block}
.share-red{background:#e04a39;color:#fff;padding:2px 3px;border-radius:2px;margin:3px 0 0}
.share-red i{background:#fff}

/* article */
.article{position:absolute;left:137px;top:370px;width:443px;font-size:10.5px;line-height:16.5px}
.article h1{font-family:"Libre Baskerville",Georgia,serif;font-size:19px;color:#333;font-weight:700;height:40px;padding-top:2px}
.article p{margin-bottom:16px;text-align:justify}
.article ul{margin:-1px 0 16px 14px;list-style:none}
.article ul li::before{content:"";display:inline-block;width:4px;height:4px;border-radius:50%;background:#333;margin-right:8px;vertical-align:middle}
.continue{display:block;text-align:right;font-size:11.5px;margin-top:-4px}

.ph-chart{float:left;width:157px;height:293px;margin:0 20px 12px 0;border:2px solid #d5d5d5;background:#fff;padding:6px 6px 0;position:relative}
.ph-head{display:flex;justify-content:space-between;font-size:4.3px;line-height:5.5px;font-weight:700;color:#333;height:38px}
.ph-head span:first-child{width:40px}
.ph-head span:last-child{width:70px;text-align:right}
.ph-row{display:flex;align-items:center;height:13.6px;font-size:4.3px;line-height:5px;color:#333}
.ph-row .conc{width:33px;text-align:right;padding-right:3px}
.ph-row .lvl{width:31px;height:12px;color:#fff;font-size:7px;font-weight:700;display:flex;align-items:center;justify-content:center;margin-right:4px}
.ph-cap{position:absolute;left:0;right:0;bottom:4px;text-align:center;font-style:italic;font-size:8.3px;line-height:15px;color:#444}

/* footer */
.footer-rule{position:absolute;left:122px;top:1105px;width:675px;height:1px;background:var(--rule)}
.footer-brand{left:122px;top:1114px}
.footer-meta{position:absolute;right:121px;top:1118px;text-align:right;font-size:8.5px;color:#333}
.footer-nav{margin-top:6px;display:flex;justify-content:flex-end;font-size:10px}
.footer-nav a{padding:0 8px;border-left:1px solid var(--rule)}
.footer-nav a:first-child{border-left:0}
.footer-nav a:last-child{padding-right:0}
.chat-tab{position:absolute;left:12px;top:1170px;width:106px;height:34px;background:#1d1d1d;color:#fff;font-size:9.5px;font-weight:600;border-radius:8px 8px 0 0;padding:9px 0 0 12px}
.chat-tab b{margin-left:10px;font-size:13px}
</style>
</head>
<body>

<header>
  <div class="brand site-brand">
    <div class="brand-dot"></div>
    <div>
      <div class="brand-name">PUREBROOK<br>FILTER GUIDE</div>
      <div class="brand-tag">Find the perfect Water Ionizer.</div>
    </div>
  </div>
  <nav class="main-nav">
    <a href="#">HOME</a><a href="#">REVIEWS</a><a href="#">LEARN</a><a href="#">COMPARE</a><a href="#">BLOG</a><a href="#">ABOUT US</a>
  </nav>
  <a class="btn-guide" href="#">Buyer’s Guide</a>
</header>

<section class="hero">
  <div class="hero-art" role="img" aria-label="Banner photo of a splashing blue water wave"></div>
  <div class="hero-bottles" role="img" aria-label="Photo of a water bottle and a filter pitcher"></div>
  <h2 class="hero-title">UNDERSTANDING THE SCIENCE &amp;<br>BENEFITS OF ALKALINE WATER</h2>
  <p class="hero-sub">The Powerful Health Benefits<br>of Ionized H<sub style="font-size:7px">2</sub>O</p>
</section>

<aside>
  <div class="lead-form">
    <div class="band">START HERE!</div>
    <h3>Download your<br>free Buyer's Guide<br>now!</h3>
    <div class="field"><label>Name:</label><span></span></div>
    <div class="field"><label>E-mail:</label><span></span></div>
    <div class="field"><label>Phone:</label><span></span></div>
    <a class="btn-download" href="#">Download</a>
  </div>

  <div class="learn-box">
    <div class="band">LEARN</div>
    <ul>
      <li><a href="#">What is Alkaline Water?</a></li>
      <li><a href="#">Benefits of Alkaline Water</a></li>
      <li><a href="#">What is Acidic Water?</a></li>
      <li><a href="#">Benefits of Acidic Water</a></li>
      <li><a href="#">What are pH and ORP?</a></li>
      <li><a href="#">How do Ionizers work?</a></li>
    </ul>
  </div>

  <div class="ad-label">Advertisements</div>
  <div class="ad ad-lifestyle">
    <div class="ad-art" role="img" aria-label="Illustration of a green leafy sprout"></div>
    <div class="ad-head">CLEARWELL<br>&nbsp;&nbsp;&nbsp;&nbsp;LIVING</div>
    <div class="ad-word w-nutrition">nutrition</div>
    <div class="ad-word w-fitness">fitness</div>
    <div class="ad-word w-mind">mind &amp; spirit</div>
    <a class="btn-join" href="#">Join Today!</a>
  </div>

  <div class="ad ad-deals">
    <div class="deal-top">Find the <b>BEST DEALS</b><br>on Water Ionizers</div>
    <div class="guarantee">GUARANTEED</div>
    <div class="product" role="img" aria-label="Product photo of two countertop water ionizers"></div>
    <div class="talk">Talk to an expert today!</div>
    <div class="phone">(800) 555 - 0147</div>
    <div class="web">filterhelpdesk-example.com</div>
  </div>
</aside>

<div class="share-col">
  <div class="count">37</div>
  <div class="share-btn"><i></i>Like</div>
  <div class="count">1</div>
  <div class="share-btn"><i></i>Tweet</div>
  <div class="count">8</div>
  <div class="share-btn"><i></i>+1</div>
  <div class="count" style="font-size:12px">343</div>
  <div class="share-btn share-red"><i></i>Share</div>
</div>

<main class="article">
  <h1>What is Alkaline Water?</h1>
  <figure class="ph-chart">
    <div class="ph-head"><span>Concentration of Hydrogen ions compared to distilled water</span><span>Examples of Solutions at this pH</span></div>
    <div class="ph-row"><span class="conc">10,000,000</span><span class="lvl" style="background:#e8141b">pH = 0</span>Battery acid</div>
    <div class="ph-row"><span class="conc">1,000,000</span><span class="lvl" style="background:#ee3124">pH = 1</span>Stomach acid</div>
    <div class="ph-row"><span class="conc">100,000</span><span class="lvl" style="background:#f36c21">pH = 2</span>Lemon juice, vinegar</div>
    <div class="ph-row"><span class="conc">10,000</span><span class="lvl" style="background:#f7a41c">pH = 3</span>Grapefruit, orange juice</div>
    <div class="ph-row"><span class="conc">1,000</span><span class="lvl" style="background:#f3e600">pH = 4</span>Tomato juice, acid rain</div>
    <div class="ph-row"><span class="conc">100</span><span class="lvl" style="background:#8dc63f">pH = 5</span>Black coffee</div>
    <div class="ph-row"><span class="conc">10</span><span class="lvl" style="background:#1a9a48">pH = 6</span>Urine, saliva</div>
    <div class="ph-row"><span class="conc">1</span><span class="lvl" style="background:#1f6bb5">pH = 7</span>Pure water</div>
    <div class="ph-row"><span class="conc">1/10</span><span class="lvl" style="background:#2d3e98">pH = 8</span>Sea water</div>
    <div class="ph-row"><span class="conc">1/100</span><span class="lvl" style="background:#5b2d90">pH = 9</span>Baking soda</div>
    <div class="ph-row"><span class="conc">1/1,000</span><span class="lvl" style="background:#8a2a90">pH = 10</span>Milk of magnesia</div>
    <div class="ph-row"><span class="conc">1/10,000</span><span class="lvl" style="background:#b3228e">pH = 11</span>Ammonia solution</div>
    <div class="ph-row"><span class="conc">1/100,000</span><span class="lvl" style="background:#d4208a">pH = 12</span>Soapy water</div>
    <div class="ph-row"><span class="conc">1/1,000,000</span><span class="lvl" style="background:#e61b7c">pH = 13</span>Bleach, oven cleaner</div>
    <div class="ph-row"><span class="conc">1/10,000,000</span><span class="lvl" style="background:#e8174f">pH = 14</span>Liquid drain cleaner</div>
    <figcaption class="ph-cap">A chart showing the different levels<br>of Acidity and pH in water.</figcaption>
  </figure>
  <p>The Water Ionizer industry is chalked full of confusing information. They often throw around machine specifications and technical jargon that needs to be dissected and explained in order to be understood. Our team at Purebrook Filter Guide is hoping to avoid this by giving you only the facts you need. We have written this information coherently so you may understand the properties of alkaline water and how it benefits you. We want your next Water Ionizer purchase to be clear and informed. So let’s start with the basics, what exactly is alkaline water?</p>
  <p>Simply put, alkaline water is water with a potential hydrogen (pH) value of more than 7 (7 being neutral on the pH scale). Typically in the water ionizer industry, this is achieved using a process known as “electrodialysis”.</p>
  <p style="clear:both">This process splits the neutral water into 2 types, acidic and alkaline. Both have their unique benefits and properties, but alkaline water is filled with <b>healthy minerals like</b>:</p>
  <ul><li>Calcium</li><li>Magnesium</li><li>Potassium</li></ul>
  <p>While unhealthy minerals like fluoride, nitrates, and sulfides, are flushed out through the acidic water.</p>
  <p>Besides the ability to eliminate the harmful toxins that are found in most tap water, there are numerous health benefits to alkaline water – all of which are backed by research. Leaders in the health and fitness industry have attested to the advantages of alkaline water for years. Maybe it’s time you discovered the real power of Alkaline Water for yourself?</p>
  <a class="continue" href="#">Continue Reading to Discover the Benefits of Alkaline Water →</a>
</main>

<footer>
  <div class="footer-rule"></div>
  <div class="brand footer-brand">
    <div class="brand-dot"></div>
    <div>
      <div class="brand-name">PUREBROOK<br>FILTER GUIDE</div>
      <div class="brand-tag">Find the perfect Water Ionizer.</div>
    </div>
  </div>
  <div class="footer-meta">
    © 2009-2012 Purebrook Filter Guide. All Rights Reserved | Read our <a href="#">Privacy Policy</a>.
    <nav class="footer-nav"><a href="#">Home</a><a href="#">Reviews</a><a href="#">Learn</a><a href="#">Compare</a><a href="#">Blog</a><a href="#">About Us</a><a href="#">Buyer’s Guide</a></nav>
  </div>
  <div class="chat-tab">Chat with us! <b>+</b></div>
</footer>

</body>
</html>
```